Start-up braucht modernes/hochwertiges Getränkeetikett
Zielgruppe
Wir sind ein modernes, nachhaltiges Start-up, welches eine neue Getränkekategorie auf den Markt bringt. Ein sogenanntes Elektrolyt-Getränk mit dem Namen KLORV5. Es ist abgefüllt in eine 500 ml Flasche und enthält Magnesium, Kalzium, Kalium, und Natrium. Diese Stoffe (Elektrolyte) dienen der körperlichen Hydrierung. Zu Dehydrierung kann es durch Hitze, Alkohol, Sport oder Krankheit kommen. Krankheit liegt bei uns allerdings nicht im Fokus. In unserer Zielgruppe befinden sich hauptsächlich Personen im Alter von 18 - 29 Jahren.
Die Geschmacksrichtung ist Zitrone-Limette.
Aufgabenstellung
Das Etikett soll:
- MODERN, SCHLICHT und HOCHWERTIG sein, so dass es im Supermarkt hervorsticht
- erkenntlich machen, dass die Stoffe Magnesium, Natrium, Kalzium und Kalium enthalten sind
- sich farblich deutlich von der Farbe des Inhalts (weiß) abheben. (Vorzugsweise mit einem hellen Blau, türkis)
- für unsere junge Zielgruppe ansprechend sein
- ebenfalls auf die Geschmacksrichtung (Zitrone-Limette) hinweisen, und zwar so, dass wenn man eine weitere Geschmacksrichtung auf den Markt bringen möchte, diese leicht angepasst werden kann.
- nicht nach einem Energydrink oder einem typischen Sportgetränk aussehen
- unter dem Namen den Slogan 'Elektrolyt-Getränk' stehen haben
-Das Etikett ist nicht dursichtig sondern besteht aus Papier
Der Name sowie das Logo können selbstverständlich farblich verändert werden. Bei dem Logo können auch größere Änderungen vollzogen werden.
Bitte beachten Sie die unten zu stehenden Regler um sich einen guten Überblick über unsere Vorstellungen zu verschaffen. Die Platzierung des EAN-Code ist für ihr Design irrelevat .
Bei Unklarheiten gerne nachfragen!

```html
<!DOCTYPE html>
<html lang="de">
<head>
<meta charset="utf-8">
<title>KLORV5 Elektrolyt-Getränk Etikett</title>
<link href="https://fonts.googleapis.com/css2?family=Saira+Semi+Condensed:wght@300;400;600;700&family=Montserrat:wght@600;700&display=swap" rel="stylesheet">
<style>
  :root {
    --page: #ffffff;
    --teal-light: #b1d7cf;
    --teal-mid: #9fd3cb;
    --teal-deep: #70cac6;
    --teal-text: #3fb6b4;
    --teal-dark: #1a9e9c;
    --pattern: #52c3c7;
    --pattern-muted: #6aaec0;
    --white: #ffffff;
    --flavour: #dcdc00;
  }
  html, body {
    margin: 0;
    padding: 0;
    width: 719px;
    height: 1200px;
    overflow: hidden;
    background: var(--page);
  }
  .canvas {
    position: relative;
    width: 719px;
    height: 1200px;
  }
  .label {
    position: absolute;
    left: 50px;
    top: 465px;
    width: 619px;
    height: 270px;
    overflow: hidden;
  }
  .label svg { display: block; }
  .headline {
    font-family: "Saira Semi Condensed", sans-serif;
    font-weight: 400;
    font-size: 15px;
    letter-spacing: 0.6px;
    fill: var(--white);
  }
  .brand-name {
    font-family: "Saira Semi Condensed", sans-serif;
    font-weight: 700;
    font-size: 11px;
    letter-spacing: 0.4px;
    fill: var(--teal-text);
  }
  .element-symbol {
    font-family: "Saira Semi Condensed", sans-serif;
    font-weight: 700;
    font-size: 11px;
    fill: var(--white);
  }
  .element-name {
    font-family: "Saira Semi Condensed", sans-serif;
    font-weight: 300;
    font-size: 7.6px;
    fill: var(--white);
  }
  .flavour-name {
    font-family: "Saira Semi Condensed", sans-serif;
    font-weight: 700;
    font-size: 10.5px;
    letter-spacing: 0.3px;
    fill: var(--white);
  }
  .volume {
    font-family: "Montserrat", sans-serif;
    font-weight: 600;
    font-size: 6.5px;
    fill: var(--teal-dark);
  }
</style>
</head>
<body>
<div class="canvas">
  <div class="label">
    <svg width="619" height="270" viewBox="0 0 619 270" xmlns="http://www.w3.org/2000/svg">
      <defs>
        <linearGradient id="label-bg" x1="0" y1="0" x2="1" y2="0.35">
          <stop offset="0" stop-color="var(--teal-light)"/>
          <stop offset="0.45" stop-color="var(--teal-mid)"/>
          <stop offset="0.72" stop-color="var(--teal-deep)"/>
          <stop offset="1" stop-color="var(--teal-deep)"/>
        </linearGradient>
        <radialGradient id="pattern-top" cx="0.85" cy="0.2" r="0.6">
          <stop offset="0" stop-color="var(--pattern)" stop-opacity="0.55"/>
          <stop offset="1" stop-color="var(--pattern)" stop-opacity="0"/>
        </radialGradient>
        <radialGradient id="pattern-bottom" cx="0.25" cy="0.9" r="0.7">
          <stop offset="0" stop-color="var(--pattern-muted)" stop-opacity="0.5"/>
          <stop offset="1" stop-color="var(--pattern-muted)" stop-opacity="0"/>
        </radialGradient>
        <filter id="hex-shadow" x="-30%" y="-30%" width="160%" height="170%">
          <feDropShadow dx="0" dy="3" stdDeviation="3" flood-color="#2a8f8c" flood-opacity="0.3"/>
        </filter>
        <polygon id="hex-small" points="0,-28.6 24.8,-14.3 24.8,14.3 0,28.6 -24.8,14.3 -24.8,-14.3"/>
      </defs>

      <!-- label background -->
      <rect class="label-bg" width="619" height="270" fill="url(#label-bg)"/>
      <rect class="lower-band" y="214" width="619" height="56" fill="var(--teal-deep)" opacity="0.35"/>

      <!-- soft decorative areas -->
      <rect class="decor-top-right" role="img" aria-label="Dekoratives Wabenmuster aus Sechsecken" x="360" y="0" width="259" height="140" fill="url(#pattern-top)"/>
      <rect class="decor-bottom-left" role="img" aria-label="Dekoratives Wabenmuster aus Sechsecken" x="0" y="170" width="200" height="100" fill="url(#pattern-bottom)"/>

      <!-- divider line -->
      <line class="divider" x1="0" y1="214" x2="619" y2="214" stroke="var(--white)" stroke-width="0.8" opacity="0.85"/>

      <!-- headline -->
      <text class="headline" x="311" y="62" text-anchor="middle">ELEKTROLYT-GETRÄNK</text>

      <!-- element hexagons -->
      <g class="element-hex" filter="url(#hex-shadow)">
        <use href="#hex-small" x="286" y="156" fill="var(--teal-mid)" stroke="var(--white)" stroke-width="0.7"/>
        <use href="#hex-small" x="336" y="156" fill="var(--teal-mid)" stroke="var(--white)" stroke-width="0.7"/>
        <use href="#hex-small" x="262" y="200" fill="#9dd3cb" stroke="var(--white)" stroke-width="0.7"/>
        <use href="#hex-small" x="361" y="200" fill="#86cfc8" stroke="var(--white)" stroke-width="0.7"/>
        <use href="#hex-small" x="311.5" y="200" fill="var(--flavour)" stroke="var(--white)" stroke-width="0.7"/>
      </g>

      <text class="element-symbol" x="286" y="156" text-anchor="middle">Mg</text>
      <text class="element-name" x="286" y="166" text-anchor="middle">MAGNESIUM</text>
      <text class="element-symbol" x="336" y="156" text-anchor="middle">Ca</text>
      <text class="element-name" x="336" y="166" text-anchor="middle">CALCIUM</text>
      <text class="element-symbol" x="262" y="200" text-anchor="middle">K</text>
      <text class="element-name" x="262" y="210" text-anchor="middle">KALIUM</text>
      <text class="element-symbol" x="361" y="200" text-anchor="middle">Na</text>
      <text class="element-name" x="361" y="210" text-anchor="middle">NATRIUM</text>
      <text class="flavour-name" x="311.5" y="198" text-anchor="middle">ZITRONE</text>
      <text class="flavour-name" x="311.5" y="211" text-anchor="middle">LIMETTE</text>

      <!-- brand hexagon -->
      <g class="brand-hex" filter="url(#hex-shadow)">
        <polygon points="311,72 342.2,90 342.2,126 311,144 279.8,126 279.8,90" fill="var(--white)"/>
      </g>
      <circle class="brand-circle" cx="311" cy="101" r="14.5" fill="none" stroke="var(--teal-text)" stroke-width="1"/>
      <text class="brand-name" x="311" y="131" text-anchor="middle">KLORV5</text>

      <!-- volume -->
      <text class="volume" x="311" y="261" text-anchor="middle">500 ml</text>
    </svg>
  </div>
</div>
</body>
</html>
```